Improvement of design for elearning template

Our company provides web based elearning courses for employees. We have a design layout for the different slides which can be found here: https://www.filecrate-share.com/sh/qemvirt7xnoa2lup/KLpQzRtYwMbDfHsnVcEkGaUoPi?dl=0. The content will be added later. At this point we are just looking for a design layout that works with different content types like images, text, quiz & videos. What we would ask you, is to pick randomly 1 or 2 of the elearning slides from the existing designs and suggest improvements or come up with an alternative design. The winner of the design project can work on all slides and this will be a project with a much larger budget.
Target Market(s)
Employees in large enterprises
Look and feel
Each slider illustrates characteristics of the customer's brand and the style your logo design should communicate.

```html
<!DOCTYPE html>
<html lang="en">
<head>
<meta charset="utf-8">
<title>Handling sensitive information – course start</title>
<link rel="stylesheet" href="https://fonts.googleapis.com/css2?family=Montserrat:wght@600;700&family=Nunito+Sans:wght@400;600;700&display=swap">
<style>
  :root {
    --ink: #0b2a9e;
    --navy: #0a2a8f;
    --badge-ring: #85aef0;
    --badge-core-top: #0b1f7a;
    --badge-core-bottom: #3a54c4;
    --sky-light: #f2fbff;
    --sky-mid: #dbe9fa;
    --card-top: #d9e8fb;
    --card-bottom: #effcff;
    --panel: #a9c4ef;
    --panel-light: #e6eefb;
    --floor: #84aaee;
    --floor-deep: #6c98e6;
    --white: #ffffff;
  }
  * { box-sizing: border-box; margin: 0; padding: 0; }
  html, body { width: 1200px; height: 710px; overflow: hidden; background: var(--white); }
  .slide {
    position: relative;
    width: 1200px;
    height: 710px;
    overflow: hidden;
    background: linear-gradient(160deg, var(--sky-mid) 0%, var(--sky-light) 45%, var(--sky-mid) 100%);
    font-family: "Nunito Sans", sans-serif;
    color: var(--ink);
  }
  .backdrop, .scene-art { position: absolute; left: 0; top: 0; width: 1200px; height: 710px; }
  .main-nav {
    position: absolute;
    top: 47px;
    left: 792px;
    display: flex;
    gap: 22px;
    font-family: "Montserrat", sans-serif;
    font-weight: 700;
    font-size: 18px;
    color: var(--navy);
  }
  .nav-item { display: flex; align-items: center; gap: 4px; }
  .nav-item svg { width: 14px; height: 8px; margin-top: 4px; }
  .intro-card {
    position: absolute;
    left: 28px;
    top: 106px;
    width: 574px;
    height: 574px;
    border-radius: 120px;
    background: linear-gradient(150deg, var(--card-top) 0%, var(--card-bottom) 70%);
    box-shadow: 4px 8px 8px rgba(30, 40, 80, 0.35);
  }
  .welcome {
    position: absolute;
    left: 89px;
    top: 42px;
    font-size: 34px;
    font-weight: 400;
    letter-spacing: 0.5px;
  }
  .course-title {
    position: absolute;
    left: 89px;
    top: 96px;
    font-size: 38px;
    font-weight: 600;
    line-height: 45px;
    letter-spacing: 2px;
  }
  .facts {
    position: absolute;
    left: 42px;
    top: 214px;
    display: flex;
    gap: 34px;
    list-style: none;
  }
  .fact {
    width: 96px;
    height: 96px;
    border-radius: 50%;
    background: var(--badge-ring);
    display: flex;
    align-items: center;
    justify-content: center;
    box-shadow: 3px 4px 5px rgba(30, 40, 80, 0.4);
  }
  .fact-core {
    width: 75px;
    height: 75px;
    border-radius: 50%;
    background: radial-gradient(circle at 50% 30%, var(--badge-core-top) 40%, var(--badge-core-bottom) 100%);
    color: var(--white);
    font-size: 11.5px;
    line-height: 17px;
    text-align: center;
    display: flex;
    flex-direction: column;
    justify-content: center;
  }
  .fact-core .label { font-size: 13px; line-height: 16px; }
  .start-button {
    position: absolute;
    left: 198px;
    top: 396px;
    width: 180px;
    height: 51px;
    border: none;
    border-radius: 14px;
    background: linear-gradient(180deg, #3a56c8 0%, #1d3aa8 100%);
    color: var(--white);
    font-family: "Nunito Sans", sans-serif;
    font-size: 33px;
    font-weight: 600;
    letter-spacing: 7px;
    padding-left: 6px;
    box-shadow: 2px 4px 5px rgba(30, 40, 80, 0.45);
  }
</style>
</head>
<body>
<main class="slide">
  <svg class="backdrop" viewBox="0 0 1200 710" aria-hidden="true">
    <path d="M0 75 C 150 40, 330 60, 600 130 L 600 0 L 0 0 Z" fill="#ffffff" opacity="0.55"/>
    <path d="M300 0 C 450 40, 560 100, 640 200 L 640 0 Z" fill="#ffffff" opacity="0.35"/>
  </svg>

  <svg class="scene-art" viewBox="0 0 1200 710" role="img" aria-label="Illustration of two colleagues beside floating screens with a padlock and a security shield, and a potted plant">
    <defs>
      <linearGradient id="floorFade" x1="0" y1="0" x2="0" y2="1">
        <stop offset="0" stop-color="#7ea8ec"/>
        <stop offset="1" stop-color="#c9dcf8"/>
      </linearGradient>
      <linearGradient id="mistFade" x1="0" y1="0" x2="0" y2="1">
        <stop offset="0" stop-color="#ffffff" stop-opacity="0"/>
        <stop offset="1" stop-color="#ffffff" stop-opacity="0.9"/>
      </linearGradient>
    </defs>
    <path d="M700 0 L 1200 0 L 1200 320 C 1100 380, 900 390, 780 330 L 700 200 Z" fill="#c6d9f5" opacity="0.6"/>
    <path d="M632 0 L 806 0 L 806 150 L 632 120 Z" fill="var(--panel)" opacity="0.7"/>
    <path d="M648 40 L 680 56 L 680 130 L 648 116 Z" fill="#8fb1ec" opacity="0.8"/>
    <path d="M690 62 L 722 78 L 722 140 L 690 126 Z" fill="#8fb1ec" opacity="0.8"/>
    <path d="M760 18 Q 752 12 752 26 L 752 300 L 918 400 Q 926 404 926 396 L 926 110 Z" fill="var(--panel-light)" opacity="0.85"/>
    <path d="M800 260 L 922 330 L 922 440 L 800 370 Z" fill="var(--panel)" opacity="0.6"/>
    <path d="M990 100 L 1190 200 L 1190 440 L 1075 380 L 990 330 Z" fill="var(--panel)" opacity="0.55"/>
    <path d="M1072 300 L 1188 360 L 1188 440 L 1072 380 Z" fill="#d6e4fa" opacity="0.8"/>
    <ellipse cx="900" cy="575" rx="310" ry="80" fill="url(#floorFade)"/>
    <path d="M700 530 C 820 495, 1000 490, 1200 500 L 1200 600 C 1050 560, 850 540, 700 560 Z" fill="var(--floor-deep)" opacity="0.35"/>
    <rect x="600" y="600" width="600" height="110" fill="url(#mistFade)"/>
    <path d="M0 690 C 200 600, 500 590, 1200 700" fill="none" stroke="#ffffff" stroke-width="2" opacity="0.8"/>
    <path d="M40 710 C 260 630, 600 620, 1200 680" fill="none" stroke="#ffffff" stroke-width="1.5" opacity="0.7"/>
  </svg>

  <nav class="main-nav">
    <span class="nav-item"><svg viewBox="0 0 14 8"><path d="M1 1 L7 6 L13 1" fill="none" stroke="currentColor" stroke-width="2"/></svg>Lessons</span>
    <span class="nav-item"><svg viewBox="0 0 14 8"><path d="M1 1 L7 6 L13 1" fill="none" stroke="currentColor" stroke-width="2"/></svg>Menu</span>
    <span class="nav-item"><svg viewBox="0 0 14 8"><path d="M1 1 L7 6 L13 1" fill="none" stroke="currentColor" stroke-width="2"/></svg>Glossary</span>
  </nav>

  <section class="intro-card">
    <p class="welcome">Wellcome to the cours</p>
    <h1 class="course-title">Handling sensitivite<br>information</h1>
    <ul class="facts">
      <li class="fact"><div class="fact-core"><span class="label">Duration</span><span>30 min</span></div></li>
      <li class="fact"><div class="fact-core"><span class="label">complexity</span><span>Medium</span></div></li>
      <li class="fact"><div class="fact-core"><span class="label">audience</span><span>All</span></div></li>
      <li class="fact"><div class="fact-core"><span class="label">interactive</span><span>Yes</span></div></li>
    </ul>
    <button class="start-button" type="button">START</button>
  </section>
</main>
</body>
</html>
```